SupplierLens720 Business Card Design

Design double sided premium business card – we will print on heavy card stock. Would like an edgy eye-catchcing card in Spot UV and/or Embossed or Foil. Something that will be memorable to our clients and new prospects
PLEASE NOTE: I have attached a word document with a more detailed overview, instructions and ideas. please review this and send a message if you have any questions

Industry/Entity Type

Financial Service

Contact Information for Business Card

would prefer to have Spot UV and/or Embossed or Foil (but no gold or silver- if you do foil only colored)

Requirements
Must have
• 1) Tagline: Redefining the way you search, qualify & manage vendors
• 2) Color Front of Card: Open to any color combo
• 3) Color on back of card: would prefer white so the contact information is easy to read
• 4) A creative design aspect.. the eye is an idea but not imperative. if you have another creative idea that represents supplierlens720 please do so. We are open to other design ideas.
Nice to have
• If you can use the words on the card as shown on my instruction document that would be nice ... I like example 1 and 1A on the logo ideas I put on the instruction document.
Should not have
• 1) We DO NOT want an all black card. (front and back)
• 2) We do not want a basic card that has the logo on front- we want some type of design incorporated on the card. - we would like something creative to grab attention.
• Note: I have attached examples of other card designs on our instruction document we attached please review and create something eye-catching like these.

```html
<!DOCTYPE html>
<html lang="en">
<head>
<meta charset="utf-8">
<title>SupplierLens720 Business Card</title>
<link rel="stylesheet" href="https://fonts.googleapis.com/css2?family=Lato:wght@400;700;900&display=swap">
<style>
  :root {
    --stage: #2b2b2d;
    --front-deep: #0d1b2c;
    --front-mid: #163a5f;
    --back-paper: #ffffff;
    --brand-blue: #1f6fc6;
    --brand-green: #7cc142;
    --ink-light: #f2f4f7;
    --ink-dark: #2a2d33;
    --ink-muted: #5b616b;
    --rule: #c4c8ce;
  }
  * { box-sizing: border-box; margin: 0; padding: 0; }
  html, body {
    width: 1200px;
    height: 900px;
    overflow: hidden;
    background: var(--stage);
    font-family: "Lato", Arial, sans-serif;
  }
  .stage {
    position: relative;
    width: 1200px;
    height: 900px;
  }
  .card {
    position: absolute;
    left: 290px;
    width: 620px;
    height: 354px;
    box-shadow: 0 12px 32px rgba(0,0,0,0.5);
    overflow: hidden;
  }
  .card--front {
    top: 70px;
    background: linear-gradient(135deg, var(--front-deep) 0%, var(--front-mid) 100%);
  }
  .card--back {
    top: 476px;
    background: var(--back-paper);
  }

  /* front side */
  .front-glow {
    position: absolute;
    left: 140px;
    top: 20px;
    width: 460px;
    height: 300px;
    border-radius: 50%;
    background: radial-gradient(ellipse at 55% 45%, rgba(180,200,220,0.42) 0%, rgba(120,150,180,0.2) 42%, rgba(20,40,60,0) 72%);
  }
  .front-orbits {
    position: absolute;
    left: 0;
    top: 0;
    width: 620px;
    height: 354px;
  }
  .brand-name {
    font-weight: 700;
    color: var(--brand-blue);
    letter-spacing: 0.5px;
    white-space: nowrap;
  }
  .card--front .brand-name {
    position: absolute;
    left: 0;
    right: 0;
    top: 128px;
    text-align: center;
    font-size: 46px;
    color: var(--ink-light);
  }
  .tagline {
    position: absolute;
    left: 0;
    right: 0;
    top: 196px;
    text-align: center;
    font-size: 15px;
    letter-spacing: 0.6px;
    color: var(--brand-green);
  }

  /* back side */
  .card--back .brand-name {
    position: absolute;
    left: 36px;
    top: 150px;
    font-size: 30px;
  }
  .back-band {
    position: absolute;
    left: 0;
    bottom: 0;
    width: 620px;
    height: 12px;
    background: linear-gradient(90deg, var(--brand-blue) 0%, var(--brand-green) 100%);
  }
  .divider {
    position: absolute;
    left: 318px;
    top: 44px;
    width: 1px;
    height: 252px;
    background: var(--rule);
  }
  .contact {
    position: absolute;
    left: 338px;
    top: 50px;
    right: 16px;
    color: var(--ink-dark);
  }
  .contact__name {
    font-weight: 700;
    font-size: 30px;
    letter-spacing: 1.5px;
    text-transform: uppercase;
    color: var(--brand-blue);
    line-height: 1;
    white-space: nowrap;
  }
  .contact__role {
    font-size: 17px;
    margin-top: 4px;
    color: var(--ink-muted);
  }
  .contact__address {
    font-size: 16px;
    line-height: 1.45;
    margin-top: 18px;
  }
  .contact__list {
    list-style: none;
    margin-top: 12px;
    font-size: 17px;
    line-height: 1.6;
  }
  .contact__list li {
    display: flex;
    align-items: center;
    gap: 10px;
    white-space: nowrap;
  }
  .contact__icon {
    width: 12px;
    height: 12px;
    flex: none;
  }
  .accent { color: var(--brand-blue); }
</style>
</head>
<body>
<main class="stage">

  <section class="card card--front" aria-label="Card front">
    <div class="front-glow" role="img" aria-label="Glowing halftone dot sphere behind the brand name"></div>
    <svg class="front-orbits" viewBox="0 0 620 354" aria-hidden="true">
      <path d="M40 300 Q310 200 590 290" fill="none" stroke="var(--brand-green)" stroke-width="3" opacity="0.85"/>
      <path d="M20 326 Q310 232 610 318" fill="none" stroke="var(--brand-blue)" stroke-width="2" opacity="0.8"/>
    </svg>
    <div class="brand-name">SupplierLens720</div>
    <p class="tagline">Redefining the way you search, qualify &amp; manage vendors</p>
  </section>

  <section class="card card--back" aria-label="Card back">
    <div class="brand-name">SupplierLens720</div>
    <div class="divider"></div>
    <div class="contact">
      <p class="contact__name">Daniel Hart</p>
      <p class="contact__role">Director</p>
      <p class="contact__address">4410 N. Canyon Ridge Dr.<br>STE B-2 #208 Tempe, AZ 85281</p>
      <ul class="contact__list">
        <li>
          <svg class="contact__icon" viewBox="0 0 12 12" aria-hidden="true"><path d="M2.5 1 L4.5 1 L5.2 3.6 L3.9 4.6 Q5 7 7.4 8.1 L8.4 6.8 L11 7.5 L11 9.5 Q11 11 9.5 11 Q1 10.5 1 2.5 Q1 1 2.5 1 Z" fill="var(--brand-blue)"/></svg>
          <span>(480) 555-0147</span>
        </li>
        <li>
          <svg class="contact__icon" viewBox="0 0 12 12" aria-hidden="true"><rect x="0.8" y="2.3" width="10.4" height="7.4" fill="none" stroke="var(--brand-blue)" stroke-width="1.2"/><path d="M0.8 2.5 L6 6.6 L11.2 2.5" fill="none" stroke="var(--brand-blue)" stroke-width="1.2"/></svg>
          <span>inquiry@supplierlens720.com</span>
        </li>
        <li>
          <svg class="contact__icon" viewBox="0 0 12 12" aria-hidden="true"><circle cx="6" cy="6" r="5" fill="none" stroke="var(--brand-blue)" stroke-width="1.1"/><ellipse cx="6" cy="6" rx="2.2" ry="5" fill="none" stroke="var(--brand-blue)" stroke-width="1"/><path d="M1 6 H11" stroke="var(--brand-blue)" stroke-width="1"/></svg>
          <span>www.<span class="accent">supplierlens720</span>.com</span>
        </li>
      </ul>
    </div>
    <div class="back-band"></div>
  </section>

</main>
</body>
</html>
```